Flyer design for our aerial photography service

We need an 8.5x11 two sided design flyer that will showcase our aerial photography service. No pricing or text is needed aside from our logo and somewhere on the page the title "Aerial Photography". I would like it be a black background with our logo in white which I have attached. Please make it a creative stylish design that highlights the photos. Our Logo should be at the top. The logo should not be large and shouldnt be the focus of the page but should be fairly visible. I'm open to it being in different locations as well.

Industry/Entity Type

Real Estate

Font styles to use
Serif

Requirements
Must have
• Logo and photos and the title Aerial Photography
Nice to have
Should not have
• n/a

```html
<!DOCTYPE html>
<html lang="en">
<head>
<meta charset="utf-8">
<title>Aerial Photography Flyer</title>
<link rel="stylesheet" href="https://fonts.googleapis.com/css2?family=Almendra:wght@400;700&family=Arimo:wght@400;700&display=swap">
<style>
  :root {
    --stage: #e6e6e6;
    --sheet: #000000;
    --frame: #5a5a5a;
    --white: #ffffff;
    --band: #8e1119;
    --band-dark: #6a0c12;
    --link: #c4222c;
  }
  * { box-sizing: border-box; margin: 0; padding: 0; }
  html, body { width: 1200px; height: 960px; overflow: hidden; }
  body {
    background: radial-gradient(circle at 60% 30%, #f6f6f6, var(--stage));
    font-family: "Arimo", Arial, sans-serif;
  }
  .flyer {
    position: absolute;
    left: 252px; top: 30px;
    width: 696px; height: 900px;
    background: var(--sheet);
    box-shadow: 0 6px 20px rgba(0,0,0,.25);
    overflow: hidden;
  }
  .flyer__title {
    position: absolute;
    left: 36px; top: 22px;
    font-family: "Almendra", Georgia, serif;
    font-size: 36px;
    color: var(--white);
    letter-spacing: .5px;
  }
  .gallery {
    position: absolute;
    left: 20px; top: 78px;
    width: 656px; height: 632px;
    display: grid;
    grid-template-columns: 1fr 1fr;
    grid-template-rows: repeat(4, 1fr);
    gap: 10px;
  }
  .gallery__photo {
    border: 7px solid var(--frame);
  }
  .photo--dusk-house   { background: linear-gradient(170deg, #6f7e86 0%, #c9b78c 40%, #3f6b2c 70%, #2f5a22 100%); }
  .photo--autumn-drive { background: linear-gradient(160deg, #b8893f 0%, #8e98a2 40%, #3a3d40 75%, #9a3a1e 100%); }
  .photo--wooded-estate{ background: linear-gradient(170deg, #2d4a24 0%, #3a5f2c 45%, #1f3b4a 60%, #2a4a20 100%); }
  .photo--spruce-home  { background: linear-gradient(165deg, #4a6a3a 0%, #9aa3a8 40%, #5d7f3c 70%, #3c5b2a 100%); }
  .photo--lake-garage  { background: linear-gradient(170deg, #3f5f3a 0%, #5d8fa0 30%, #6e6b66 60%, #474645 100%); }
  .photo--white-home   { background: linear-gradient(165deg, #3d5a2e 0%, #d6d6d2 40%, #6e6660 60%, #4f7a34 100%); }
  .photo--fall-valley  { background: linear-gradient(160deg, #6e5a3e 0%, #c7712a 35%, #d4a32a 55%, #4d6c2e 80%, #3a3a3a 100%); }
  .photo--lakeshore    { background: linear-gradient(175deg, #2f5a24 0%, #3c6a2c 45%, #b9a98a 55%, #2d5a4e 70%, #1f4a45 100%); }

  .flyer__footer {
    position: absolute;
    left: 20px; right: 20px; top: 724px;
    height: 130px;
  }
  .brand {
    position: absolute;
    left: 16px; bottom: 8px;
    display: flex; align-items: center; gap: 12px;
  }
  .brand__mark {
    width: 46px; height: 46px;
    border-radius: 50%;
    background: var(--white);
  }
  .brand__name {
    color: var(--white);
    font-size: 22px;
    font-weight: 400;
    letter-spacing: 2px;
    text-transform: uppercase;
  }
  .contact {
    position: absolute;
    right: 4px; top: 4px;
    text-align: right;
    color: var(--white);
    font-size: 14px;
    line-height: 1.45;
  }
  .contact__web {
    position: absolute;
    right: 4px; bottom: 8px;
    color: var(--link);
    font-size: 17px;
    font-weight: 700;
  }
  .flyer__band {
    position: absolute;
    left: 0; right: 0; bottom: 0;
    height: 34px;
    background: linear-gradient(180deg, var(--band), var(--band-dark));
  }
</style>
</head>
<body>
  <main class="flyer">
    <h1 class="flyer__title">Aerial Photography</h1>

    <section class="gallery">
      <div class="gallery__photo photo--dusk-house" role="img" aria-label="Two-storey house at dusk with lit windows and a green lawn"></div>
      <div class="gallery__photo photo--autumn-drive" role="img" aria-label="Grey house with paved driveway among autumn trees"></div>
      <div class="gallery__photo photo--wooded-estate" role="img" aria-label="Aerial view of a large home surrounded by dense green woods"></div>
      <div class="gallery__photo photo--spruce-home" role="img" aria-label="Grey house beside tall spruce trees and a curved driveway"></div>
      <div class="gallery__photo photo--lake-garage" role="img" aria-label="Lakeside house with a large garage roof and hills beyond"></div>
      <div class="gallery__photo photo--white-home" role="img" aria-label="White home with wraparound balconies among trees"></div>
      <div class="gallery__photo photo--fall-valley" role="img" aria-label="Aerial view of a neighbourhood with winding road and autumn foliage"></div>
      <div class="gallery__photo photo--lakeshore" role="img" aria-label="Lakeshore home with a beach, dock and boat"></div>
    </section>

    <footer class="flyer__footer">
      <div class="contact">
        <p>112 Harbor Lane, Cedar Grove, NJ 07009</p>
        <p>Telephone: +1 555 014 2280</p>
        <p>E-mail: hello@keystonelens.com</p>
      </div>
      <div class="brand">
        <span class="brand__mark"></span>
        <span class="brand__name">Keystone Lens Studio</span>
      </div>
      <p class="contact__web">www.keystonelens.com</p>
    </footer>

    <div class="flyer__band"></div>
  </main>
</body>
</html>
```